Wordpress website design for a high-end painting business

We are currently rebranding and are looking to update our Wordpress theme. We have recently rebranded our logo on PixelHarbor, and would like our website to be equally as refined.
Our business is named “Kestrel Painters”. We are a high-end painting business that is known for being professional and having high standards. Our clean and professional image is important as it separates us from our competition. Our current website can be found at www.wrenfieldcoatings.co.nz . We designed the site ourselves so it is understandably rudimentary. We are generally happy with the. page layout of our existing site, but we like a professional remodel. Any ideas on improvement welcomed.
We would like the front page of the website to summarise all of the info throughout the whole website (I.e introduction, photos, testimonials, contact info etc.) as visitors typically scroll through the first page to see that we are reputable and get to our contact number/email contact at the bottom of the page. We would like this first page to give a clean well rounded image of our business. We would like the gallery to be a scroll through of large photos, as it is difficult to see paint details in smaller photos. A contact page with an enquiry section would also be good.
For the colour scheme, we would like something that fits a bold, masculine and high end theme (similar to our logo attached).
We would like the footer to include Veltora paint logos and the accredited painter logo we have included as these are important to our profession.
We have attached some photos of our work also. I will add more in the coming days. More can also be found on our website.
If you have questions or comments, please don’t hesitate to ask and I will get back as soon as possible.
We are open to your own interpretation or ideas for a better layout/site provided they fit the general brief of being a well rounded site for our profession.
Thanks,
Kestrel Painters.
Target Market(s)
High end clients
Industry/Entity Type
Painting (interior and exterior)
Coding
Coded - Design and coding required
Requirements
Must have
- Classy feel, separating us from typical painting companies. Well rounded homepage.
Nice to have
- Lots of examples of our work
Should not have
- Untidy paint motifs (eg, paint droplets, paint splashes)

```html
<!DOCTYPE html>
<html lang="en">
<head>
<meta charset="utf-8">
<title>Kestrel Painters</title>
<link href="https://fonts.googleapis.com/css2?family=Playfair+Display:wght@400;700&family=Poppins:wght@400;500;600;700&display=swap" rel="stylesheet">
<style>
:root{
  --brown:#8c6d47;
  --brown-dark:#7a5d3a;
  --navy:#141b25;
  --ink:#1c1c1c;
  --body:#444;
  --white:#fff;
  --paper:#ececec;
  --serif:'Playfair Display', Georgia, serif;
  --sans:'Poppins', Arial, sans-serif;
}
*{margin:0;padding:0;box-sizing:border-box}
html,body{width:1200px;height:4002px;overflow:hidden}
body{position:relative;background:var(--white);font-family:var(--sans);color:var(--body)}
.abs{position:absolute}

/* header */
.brand{position:absolute;left:89px;top:12px;width:130px;text-align:center}
.brand-mark{width:70px;height:70px;border-radius:50%;background:var(--navy);margin:0 auto 10px}
.brand-name{font-family:var(--serif);font-weight:700;color:var(--navy);font-size:22px;line-height:1;letter-spacing:.5px}
.brand-name small{display:block;font-size:12px;letter-spacing:3px;margin-top:4px}
.nav{position:absolute;top:38px;left:451px;display:flex;gap:28px;align-items:center;font-size:13px;font-weight:600;color:var(--ink);letter-spacing:.3px}
.nav .home{width:14px;height:14px;fill:var(--brown)}
.call{position:absolute;left:971px;top:30px;display:flex;align-items:center;gap:8px}
.call svg{width:22px;height:22px;fill:var(--brown)}
.call span{display:block;font-size:11px;color:var(--brown);line-height:1.1}
.call strong{font-size:16px;color:var(--ink);font-weight:700}

/* hero */
.hero-kicker{left:89px;top:324px;font-weight:700;font-size:26px;color:var(--brown)}
.hero-title{left:89px;top:355px;font-family:var(--serif);font-size:72px;line-height:64px;color:var(--ink);font-weight:400}
.hero-text{left:89px;top:500px;width:400px;font-size:14px;line-height:22px}
.btn{display:inline-flex;align-items:center;gap:14px;background:var(--brown);color:var(--white);font-weight:700;font-size:13px;border-radius:24px;padding:0 22px;height:44px}
.btn::after{content:"›";font-size:18px}
.hero-btn{left:89px;top:564px}
.photo-ring{position:absolute;border-radius:50%;border:6px solid #c9d6e3;box-shadow:0 0 0 3px #fff,0 0 0 5px #aebdcc}
.hero-photo{left:536px;top:112px;width:668px;height:668px;background:linear-gradient(180deg,#6fa3d8 0%,#cdbfa4 45%,#7a9a4e 100%)}

/* about */
.about-photo{left:93px;top:789px;width:498px;height:498px;background:linear-gradient(180deg,#8fb8e0 0%,#d9d2b8 45%,#5f7d43 100%)}
.about-title{left:648px;top:905px;font-family:var(--serif);font-size:56px;line-height:70px;color:var(--ink);font-weight:400}
.about-text{left:648px;top:982px;width:445px;font-size:14px;line-height:22.5px}
.about-btn{left:645px;top:1155px}

/* services */
.services-band{left:0;top:1250px;width:1200px;height:930px}
.services-title{left:0;top:1546px;width:1200px;text-align:center;font-family:var(--serif);font-size:56px;line-height:70px;color:var(--white);font-weight:400}
.services-sub{left:0;top:1616px;width:1200px;text-align:center;font-size:16px;color:var(--white)}
.service{position:absolute;top:1684px;width:316px;height:316px;border-radius:50%;display:flex;flex-direction:column;align-items:center;justify-content:center;gap:18px;color:var(--white);font-family:var(--serif);font-size:30px;box-shadow:0 0 0 8px rgba(20,27,37,.35),0 18px 30px rgba(0,0,0,.25)}
.service svg{width:130px;height:110px;fill:none;stroke:var(--white);stroke-width:4}
.service.interior{left:262px;background:var(--brown)}
.service.exterior{left:630px;background:var(--navy)}

/* gallery */
.section-title{left:0;width:1200px;text-align:center;font-family:var(--serif);font-size:56px;line-height:70px;color:var(--ink);font-weight:400}
.gallery-title{top:2136px}
.gallery-sub{left:0;top:2206px;width:1200px;text-align:center;font-size:14px}
.shot{position:absolute;top:2258px;height:381px;border-radius:8px}
.shot-1{left:0;width:281px;background:linear-gradient(180deg,#e8e4da,#c8c2b4 60%,#2a3d6b)}
.shot-2{left:297px;width:297px;background:linear-gradient(180deg,#2f6fd0,#b8c0cf 45%,#6f9a48)}
.shot-3{left:608px;width:297px;background:#a4896a}
.shot-4{left:920px;width:280px;border-radius:8px 0 0 8px;background:linear-gradient(180deg,#e9ecee,#b8bec4 55%,#4d5058)}
.shot-overlay{position:absolute;inset:12px;border-radius:10px;background:rgba(140,109,71,.85);display:flex;flex-direction:column;align-items:center;justify-content:center;color:var(--white);font-family:var(--serif);font-weight:700;font-size:20px;text-align:center;line-height:26px}
.shot-icons{display:flex;gap:10px;margin-top:16px}
.shot-icons i{width:44px;height:44px;border-radius:50%;background:var(--white);display:flex;align-items:center;justify-content:center}
.shot-icons svg{width:16px;height:16px;fill:none;stroke:var(--ink);stroke-width:2.5}

/* testimonials */
.testi-title{top:2750px}
.quote-disc{left:230px;top:2867px;width:296px;height:296px;border-radius:50%;background:var(--paper);box-shadow:0 0 0 10px #f5f5f5;display:flex;align-items:center;justify-content:center;font-family:var(--serif);font-weight:700;font-size:300px;color:var(--brown);line-height:1}
.quote-disc span{margin-top:150px}
.testi-text{left:564px;top:2914px;width:416px;font-size:13.5px;line-height:22.5px;hyphens:auto}
.testi-name{left:567px;top:3052px;font-size:18px;font-weight:600;color:var(--ink)}
.testi-arrows{left:568px;top:3094px;display:flex;gap:18px}
.testi-arrows svg{height:22px;fill:none;stroke:var(--brown);stroke-width:2.5}

/* badges */
.badges{left:264px;top:3248px;display:flex;gap:8px;align-items:center}
.badge{height:46px;background:#8b8b8b;border-radius:2px}

/* footer */
.footer-bg{left:0;top:3360px;width:1200px;height:642px}
.foot-brand{left:89px;top:3640px;width:190px;text-align:center}
.foot-brand .brand-mark{width:110px;height:110px;background:#1f2935;margin-bottom:14px}
.foot-brand .brand-name{color:var(--white);font-size:30px}
.foot-brand .brand-name small{font-size:15px}
.foot-head{font-family:var(--serif);font-weight:700;color:var(--white);font-size:28px;top:3624px}
.foot-list{list-style:none;top:3675px;font-size:15px;color:var(--white);line-height:31px}
.foot-text{font-size:15px;color:var(--white)}
.input{left:561px;top:3706px;width:245px;height:38px;border-radius:19px;background:#242c37;color:var(--white);font-size:12px;padding-left:18px;display:flex;align-items:center}
.subscribe{left:561px;top:3753px;height:39px;width:134px;justify-content:center;padding:0;font-size:13px}
.subscribe::after{content:none}
.contact-line{display:flex;align-items:center;gap:9px;left:862px;font-size:15px;color:var(--white)}
.contact-line svg{width:15px;height:15px;fill:var(--brown)}
.foot-rule{left:89px;top:3946px;width:1022px;height:1px;background:#3a424d}
.copyright{left:0;top:3964px;width:1200px;text-align:center;color:var(--white);font-size:14px}
.to-top{left:1124px;top:3930px;width:34px;height:34px;border-radius:50%;background:var(--brown);display:flex;align-items:center;justify-content:center;color:var(--white);font-size:14px}
</style>
</head>
<body>

<header>
  <div class="brand"><div class="brand-mark"></div><div class="brand-name">KESTREL<small>PAINTERS</small></div></div>
  <nav class="nav">
    <svg class="home" viewBox="0 0 16 16"><path d="M8 1 1 8h2v7h4v-4h2v4h4V8h2z"/></svg>
    <span>SERVICES</span><span>GALLERY</span><span>ABOUT</span><span>TESTIMONIALS</span><span>CONTACT</span>
  </nav>
  <div class="call">
    <svg viewBox="0 0 24 24"><path d="M6.6 10.8a15 15 0 0 0 6.6 6.6l2.2-2.2c.3-.3.7-.4 1-.2 1.1.4 2.3.6 3.6.6.6 0 1 .4 1 1V20c0 .6-.4 1-1 1A17 17 0 0 1 3 4c0-.6.4-1 1-1h3.5c.6 0 1 .4 1 1 0 1.3.2 2.5.6 3.6.1.3 0 .7-.2 1z"/></svg>
    <div><span>CALL NOW</span><strong>021 555 0148</strong></div>
  </div>
</header>

<section class="hero">
  <div class="abs hero-kicker">WELCOME TO</div>
  <h1 class="abs hero-title">KESTREL<br>PAINTERS</h1>
  <p class="abs hero-text">We are a high-end painting business that is known for being professional and having high standards.</p>
  <a class="abs btn hero-btn">GET IN TOUCH</a>
  <div class="photo-ring hero-photo" role="img" aria-label="Photo of a large two-storey house with fresh exterior paint and a green lawn"></div>
</section>

<section class="about">
  <div class="photo-ring about-photo" role="img" aria-label="Photo of a single-storey house being repainted"></div>
  <h2 class="abs about-title">ABOUT US</h2>
  <p class="abs about-text">Here at Kestrel Painters, we take a lot of pride in our work. We strive to ensure the highest quality paint-work, paying close attention to detail to provide a long lasting finish. Our clients are always our priority, we aim to deliver beyond their expectations. It is our goal to provide an excellent service from start to finish through clear communication, free quoting and transparency with our pricing.</p>
  <a class="abs btn about-btn">READ MORE</a>
</section>

<section class="services">
  <svg class="abs services-band" viewBox="0 1250 1200 930" preserveAspectRatio="none">
    <path fill="var(--brown)" d="M0 1352C180 1390 300 1490 370 1478S560 1360 660 1320 860 1250 940 1262 1120 1300 1200 1322V2170C1060 2060 920 2000 800 1990S520 1975 390 1965 110 1990 0 2036Z"/>
  </svg>
  <h2 class="abs services-title">OUR SERVICES</h2>
  <p class="abs services-sub">We proudly use the finest quality Veltora paints on all of the projects that we work on.</p>
  <div class="service interior">
    <svg viewBox="0 0 130 110"><rect x="46" y="4" width="62" height="44" rx="6"/><path d="M50 38l18-16 14 12 10-8 14 12"/><rect x="38" y="62" width="82" height="34" rx="6"/><path d="M30 96v10M128 96v10"/><rect x="8" y="40" width="18" height="20" rx="4"/><path d="M17 60v46M6 106h22"/></svg>
    INTERIOR
  </div>
  <div class="service exterior">
    <svg viewBox="0 0 130 110"><path d="M4 40 38 8h56l32 32"/><rect x="12" y="40" width="108" height="66"/><rect x="24" y="52" width="34" height="14"/><rect x="74" y="52" width="34" height="14"/><rect x="34" y="76" width="28" height="30"/><path d="M74 78h34M74 90h34"/></svg>
    EXTERIOR
  </div>
</section>

<section class="gallery">
  <h2 class="abs section-title gallery-title">GALLERY</h2>
  <p class="abs gallery-sub">Exterior repaint in Marrow Creek, Northvale.</p>
  <div class="shot shot-1" role="img" aria-label="Photo of a bright living room with a blue carpet and white sofa"></div>
  <div class="shot shot-2" role="img" aria-label="Photo of a small grey weatherboard house under blue sky"></div>
  <div class="shot shot-3" role="img" aria-label="Photo of a painter at work inside a house">
    <div class="shot-overlay">House repaint<br>in Fenwick, Ashbury.
      <div class="shot-icons">
        <i><svg viewBox="0 0 16 16"><path d="M7 9l2-2M5 8 3 10a2 2 0 0 0 3 3l2-2M11 8l2-2a2 2 0 0 0-3-3L8 5"/></svg></i>
        <i><svg viewBox="0 0 16 16"><circle cx="7" cy="7" r="4.5"/><path d="M10.5 10.5 14 14"/></svg></i>
      </div>
    </div>
  </div>
  <div class="shot shot-4" role="img" aria-label="Photo of a white weatherboard house with a deck and outdoor chairs"></div>
</section>

<section class="testimonials">
  <h2 class="abs section-title testi-title">TESTIMONIALS</h2>
  <div class="abs quote-disc"><span>“</span></div>
  <p class="abs testi-text">These guys are great from beginning to end. Very professional, excellent businessmen, hard workers, and top-quality work. Excellent communication, do what they say they will do and more, and really go the extra mile to make the job as painless as possible. Without reservations would highly recommend!</p>
  <div class="abs testi-name">Marla Quinton (2020)</div>
  <div class="abs testi-arrows">
    <svg viewBox="0 0 12 22" width="12"><path d="M10 3 2 11l8 8"/></svg>
    <svg viewBox="0 0 28 22" width="28"><path d="M2 11h24M18 3l8 8-8 8"/></svg>
  </div>
</section>

<div class="abs badges" aria-label="Partner badges">
  <div class="badge" style="width:146px"></div>
  <div class="badge" style="width:290px;background:#9a9a9a"></div>
  <div class="badge" style="width:152px"></div>
</div>

<footer>
  <svg class="abs footer-bg" viewBox="0 3360 1200 642" preserveAspectRatio="none">
    <path fill="var(--navy)" d="M0 3480C220 3395 480 3370 720 3400S1060 3480 1200 3560V4002H0Z"/>
  </svg>
  <div class="abs foot-brand"><div class="brand-mark"></div><div class="brand-name">KESTREL<small>PAINTERS</small></div></div>

  <h3 class="abs foot-head" style="left:334px">Useful links</h3>
  <ul class="abs foot-list" style="left:334px">
    <li>Home</li><li>Services</li><li>Gallery</li><li>About</li><li>Contact</li><li>All Testimonials</li>
  </ul>

  <h3 class="abs foot-head" style="left:566px">Newsletter</h3>
  <p class="abs foot-text" style="left:566px;top:3670px">Subscribe to our newsletter</p>
  <div class="abs input">Email Address</div>
  <a class="abs btn subscribe">SUBSCRIBE</a>

  <h3 class="abs foot-head" style="left:858px">Contact Info</h3>
  <div class="abs contact-line" style="top:3670px">Rowan Ellery</div>
  <div class="abs contact-line" style="top:3704px"><svg viewBox="0 0 24 24"><path d="M6.6 10.8a15 15 0 0 0 6.6 6.6l2.2-2.2c.3-.3.7-.4 1-.2 1.1.4 2.3.6 3.6.6.6 0 1 .4 1 1V20c0 .6-.4 1-1 1A17 17 0 0 1 3 4c0-.6.4-1 1-1h3.5c.6 0 1 .4 1 1 0 1.3.2 2.5.6 3.6.1.3 0 .7-.2 1z"/></svg>021 555 0148</div>
  <div class="abs contact-line" style="top:3738px"><svg viewBox="0 0 24 24"><path d="M2 5h20v14H2zm2 2v1l8 5 8-5V7l-8 5z"/></svg>hello@kestrelpainters.example</div>
  <div class="abs contact-line" style="top:3772px">Ashbury, Northvale.</div>

  <div class="abs foot-rule"></div>
  <div class="abs to-top">⌃</div>
  <p class="abs copyright">©Copyright 2022 | All Rights Reserved</p>
</footer>

</body>
</html>
```